Norvane Builders Business Card

Modern and Professional Business Card for a Med size construction/development company.

See the samples below for the design I like … but I need ideas for incorporating the red company logo while still keeping the clean look of the card samples that are attached.

Logo and tag line on the back … info on the front.

Tagline: Quality Starts from the Ground Up

Target Market(s)

Med-Large General Contractors

Contact Information for Business Card

Norvane Builders Limited
42 Brenton Street
Elk Harbour, NL
B3K 7T2

t: 709-555-0147
f: 709-555-0192
w: www.norvanebuilders-example.com

Font styles to use
Sans Serif

Colors
fbee3e

Requirements
Must have
• I like the black and yellow designs of the attached samples …. but I'm not sure how to incorporate the red Norvane Builders logo into that design??
Nice to have
• Construction safety strips

```html
<!DOCTYPE html>
<html lang="en">
<head>
<meta charset="utf-8">
<title>Norvane Builders – Business Card</title>
<link href="https://fonts.googleapis.com/css2?family=Montserrat:wght@400;500;700&family=Oswald:wght@500&display=swap" rel="stylesheet">
<style>
  :root {
    --page-bg: #2a2a2a;
    --card-bg: #232323;
    --card-edge: #2e2e2e;
    --ink-silver: #b9b9b9;
    --ink-light: #d6d6d6;
    --ink-muted: #8d8d8d;
    --brand-red: #c8202a;
    --accent-yellow: #fbee3e;
  }
  * { margin: 0; padding: 0; box-sizing: border-box; }
  html, body {
    width: 1200px; height: 878px; overflow: hidden;
    background: var(--page-bg);
    font-family: "Montserrat", sans-serif;
  }
  .sheet { position: relative; width: 1200px; height: 878px; }
  .card {
    position: absolute; left: 250px; width: 700px; height: 400px;
    background: var(--card-bg);
    border: 1px solid var(--card-edge);
    border-radius: 22px;
    box-shadow: 0 14px 34px rgba(0,0,0,.45);
    overflow: hidden;
  }
  .card--back { top: 28px; }
  .card--front { top: 450px; }

  /* Back: company name and tagline */
  .brand {
    position: absolute; inset: 0;
    display: flex; flex-direction: column; align-items: center; justify-content: center;
    gap: 18px;
  }
  .brand__lockup { display: flex; align-items: center; gap: 14px; }
  .brand__mark { width: 22px; height: 22px; background: var(--brand-red); }
  .brand__name {
    font-weight: 700; font-size: 30px; letter-spacing: 1px;
    color: var(--brand-red); text-transform: uppercase; white-space: nowrap;
  }
  .brand__rule { width: 80px; height: 2px; background: var(--accent-yellow); }
  .brand__tagline {
    font-weight: 500; font-size: 15px; letter-spacing: 2px;
    color: var(--accent-yellow); text-transform: uppercase;
  }

  /* Front: identity */
  .identity { position: absolute; right: 372px; top: 148px; text-align: right; }
  .identity__name {
    font-family: "Oswald", sans-serif; font-weight: 500;
    font-size: 34px; letter-spacing: 2px; line-height: 1;
    color: var(--ink-silver); text-transform: uppercase; white-space: nowrap;
  }
  .identity__role { margin-top: 6px; font-size: 15px; color: var(--accent-yellow); }
  .divider {
    position: absolute; left: 348px; top: 140px; width: 2px; height: 100px;
    background: var(--accent-yellow);
  }
  .contacts { position: absolute; left: 372px; top: 148px; list-style: none; }
  .contacts li {
    display: flex; align-items: center; gap: 10px;
    font-size: 14.5px; line-height: 23px; color: var(--ink-light); white-space: nowrap;
  }
  .contacts svg { width: 11px; height: 11px; flex: none; }
  .address {
    position: absolute; left: 0; right: 0; bottom: 42px; text-align: center;
    font-size: 17px; color: var(--ink-muted); letter-spacing: .5px;
  }
</style>
</head>
<body>
<main class="sheet">
  <section class="card card--back" aria-label="Card back">
    <div class="brand">
      <div class="brand__lockup">
        <span class="brand__mark"></span>
        <span class="brand__name">Norvane Builders Limited</span>
      </div>
      <span class="brand__rule"></span>
      <p class="brand__tagline">Quality Starts from the Ground Up</p>
    </div>
  </section>

  <section class="card card--front" aria-label="Card front">
    <div class="identity">
      <p class="identity__name">Darren Holloway</p>
      <p class="identity__role">Director</p>
    </div>
    <div class="divider"></div>
    <ul class="contacts">
      <li>
        <svg viewBox="0 0 12 12" fill="none" stroke="#fbee3e" stroke-width="1.4"><path d="M2 1.5 L4 1.5 L5 4 L3.8 5 Q5 7.5 7 8.2 L8 7 L10.5 8 L10.5 10 Q6 11 3 7.5 Q1 4.5 2 1.5Z"/></svg>
        709-555-0147
      </li>
      <li>
        <svg viewBox="0 0 12 12" fill="none" stroke="#fbee3e" stroke-width="1.4"><rect x="3" y="1" width="6" height="10" rx="1"/><line x1="5.2" y1="9.2" x2="6.8" y2="9.2"/></svg>
        709-555-0192
      </li>
      <li>
        <svg viewBox="0 0 12 12" fill="none" stroke="#fbee3e" stroke-width="1.3"><rect x="1" y="2.5" width="10" height="7" rx="1"/><path d="M1.3 3 L6 6.5 L10.7 3"/></svg>
        info@norvanebuilders-example.com
      </li>
      <li>
        <svg viewBox="0 0 12 12" fill="none" stroke="#fbee3e" stroke-width="1.1"><circle cx="6" cy="6" r="4.8"/><ellipse cx="6" cy="6" rx="2" ry="4.8"/><line x1="1.2" y1="6" x2="10.8" y2="6"/></svg>
        www.norvanebuilders-example.com
      </li>
    </ul>
    <p class="address">42 Brenton Street Elk Harbour, NL B3K 7T2</p>
  </section>
</main>
</body>
</html>
```